Restaurant Menu Design for Meal Prep offered in a food display cooler at a local Gym

I am looking for a menu design with the following items . I would like a workable copy if possible so in the future we can change pricing on this file , or change items . This file will be uploaded on a USB drive and then plugged into a TV. Please ensure a JPEG file is included so this will also work on this TV.

Have a look at our website , www.quilvarkitchen.com for ideas for design that represent the brand appropriately.
The below are the menu items that we would need displayed along with their pricing.

BREAKFAST MEAL PREP ITEMS
Blueberry Pancakes $12.00
Copper Lantern Burrito $10.95

LUNCH/DINNER MEAL PREP OPTIONS
BBQ Glazed Salmon $16.50
Cheeseburger Bowl $13.50
Chicken Alfredo $12.00
Pesto Chicken Pasta $12.00
Chicken Parmesan $13.00
Taco Bowl $14.00
Steak Bite and Green Stir Fry $12.00
Asian Chicken Teriyaki $12.00
Marlowe Stir Fry $15.95

I will attach our logo below, this will need to be on the design. The "heading" (for example breakfast meal prep items and lunch/dinner meal prep options) for the menu should also be on the design.

Ive attached a couple of photos that you need to add to your design.

This will be displayed in a GYM

Meal Prep + Fitness Industry

• Quilvar Logo and Photos attached
• Maybe incorporate something that represents working out or healthy lifestyle in design without going too overboard

```html
<!DOCTYPE html>
<html lang="en">
<head>
<meta charset="utf-8">
<title>Quilvar Kitchen – Restaurant Menu</title>
<link rel="stylesheet" href="https://fonts.googleapis.com/css2?family=Montserrat:wght@400;500;600;700;800&display=swap">
<style>
  :root {
    --page-bg: #efeff2;
    --sheet-bg: #ffffff;
    --plum: #5b2a63;
    --indigo: #40396b;
    --ink: #3d3769;
    --muted: #8a8a8a;
    --rule: #c9c4d6;
    --divider: #c8c8d2;
    --food-warm: #f2c98a;
    --food-green: #8cbf5a;
    --food-plate: #e9eef5;
  }
  * { margin: 0; padding: 0; box-sizing: border-box; }
  html, body { width: 1200px; height: 1000px; overflow: hidden; }
  body {
    background: var(--page-bg);
    font-family: "Montserrat", Arial, sans-serif;
    color: var(--ink);
    position: relative;
  }
  .menu-sheet {
    position: absolute; left: 82px; top: 162px;
    width: 1036px; height: 716px;
    background: var(--sheet-bg);
  }
  .abs { position: absolute; }

  /* Cover side */
  .brand-name {
    left: 195px; top: 36px; width: 166px; text-align: center;
    font-size: 30px; font-weight: 800; letter-spacing: 1px; color: var(--indigo);
  }
  .brand-rule { left: 195px; top: 89px; width: 170px; height: 1px; background: var(--rule); }
  .brand-est {
    left: 195px; top: 98px; width: 170px; text-align: center;
    font-size: 10px; color: var(--muted); letter-spacing: .5px;
  }
  .cover-title {
    left: 76px; top: 144px; width: 400px; text-align: center;
    font-size: 30px; font-weight: 700; color: var(--indigo); letter-spacing: .5px;
  }
  .cover-tag {
    left: 233px; top: 190px; width: 88px; height: 34px;
    background: var(--plum); color: #fff;
    font-size: 21px; font-weight: 700; text-align: center; line-height: 34px;
  }
  .dish-frame {
    left: 91px; top: 277px; width: 370px; height: 303px;
    border: 2px solid var(--plum);
  }
  .dish-frame-gap { left: 186px; top: 276px; width: 182px; height: 4px; background: var(--sheet-bg); }
  .dish-gallery {
    left: 100px; top: 286px; width: 352px; height: 285px;
    border-radius: 6px;
    background: radial-gradient(circle at 30% 30%, var(--food-warm), transparent 45%),
                radial-gradient(circle at 75% 65%, var(--food-green), transparent 45%),
                var(--food-plate);
  }
  .site-url {
    left: 76px; top: 666px; width: 400px; text-align: center;
    font-size: 14px; font-weight: 500; color: var(--indigo);
  }
  .page-divider { left: 517px; top: 36px; width: 1px; height: 642px; background: var(--divider); }

  /* Menu panels */
  .panel { border: 2px solid var(--plum); }
  .panel-title {
    background: var(--sheet-bg); color: var(--plum);
    font-weight: 800; text-align: center; padding: 0 14px;
  }
  .section-tag {
    border: 2px solid var(--indigo); color: var(--indigo);
    font-size: 18px; font-weight: 500; text-align: center; letter-spacing: .3px;
  }
  .dish-thumb { border-radius: 50%; }
  .thumb-pancake { background: radial-gradient(circle, #f0b868 0 38%, #f5f5f7 40% 100%); }
  .thumb-pasta { background: radial-gradient(circle, #e99a4c 0 45%, #eef0f2 48% 100%); }

  .item-name { font-size: 14px; font-weight: 700; color: var(--indigo); line-height: 1; white-space: nowrap; }
  .item-name small { display: block; font-size: 8.5px; margin-top: 2px; }
  .item-price { font-size: 14px; font-weight: 700; color: var(--plum); white-space: nowrap; }
  .item-price.big { font-size: 16px; }
  .item-desc { font-size: 9px; line-height: 18.5px; color: var(--indigo); white-space: nowrap; }
  .col-rule { width: 2px; background: var(--indigo); }

  .line-name { font-size: 9.5px; font-weight: 500; color: var(--indigo); line-height: 12px; white-space: nowrap; }
  .line-price { font-size: 13px; font-weight: 500; color: var(--plum); text-align: right; width: 60px; }
</style>
</head>
<body>
<main class="menu-sheet">
  <!-- Cover -->
  <div class="abs brand-name">QUILVAR</div>
  <div class="abs brand-rule"></div>
  <div class="abs brand-est">ESTB 2015</div>
  <h1 class="abs cover-title">RESTAURANT</h1>
  <div class="abs cover-tag">MENU</div>
  <div class="abs dish-frame"></div>
  <div class="abs dish-frame-gap"></div>
  <div class="abs dish-gallery" role="img" aria-label="Grid of twelve illustrated dishes: pasta, steak, fries, salads, soup, pancakes and desserts"></div>
  <div class="abs site-url">www.quilvarkitchen.com</div>
  <div class="abs page-divider"></div>

  <!-- Breakfast -->
  <section class="abs panel" style="left:575px;top:44px;width:371px;height:302px;"></section>
  <h2 class="abs panel-title" style="left:670px;top:33px;width:166px;font-size:23px;">BREAKFAST</h2>
  <div class="abs dish-thumb thumb-pancake" style="left:581px;top:70px;width:76px;height:50px;" role="img" aria-label="Stack of blueberry pancakes"></div>
  <div class="abs dish-thumb thumb-pancake" style="left:860px;top:70px;width:76px;height:50px;" role="img" aria-label="Stack of blueberry pancakes"></div>
  <div class="abs section-tag" style="left:662px;top:74px;width:192px;height:42px;line-height:38px;">MEAL PREP ITEMS</div>

  <div class="abs item-name" style="left:592px;top:154px;">BLUEBERRY<small>PANCAKES</small></div>
  <div class="abs item-price" style="left:698px;top:153px;">$12.00</div>
  <p class="abs item-desc" style="left:592px;top:205px;">GLUTEN FREE PROTEIN PANCAKE<br>MIX, FRESH BLUEBERRIES,<br>BLUEBERRY YOGURT SAUCE,<br>SERVED WITH 100%<br>MAPLE SYRUP.</p>
  <div class="abs col-rule" style="left:757px;top:156px;height:154px;"></div>
  <div class="abs item-name" style="left:774px;top:154px;">COPPER<small>LANTERN BURRITO</small></div>
  <div class="abs item-price big" style="left:873px;top:153px;">$10.95</div>
  <p class="abs item-desc" style="left:774px;top:205px;">SHAVED RIB EYE STEAK, BLACK<br>BEANS, CARAMELIZED ONIONS,<br>CHERRY TOMATOES, FETA<br>CHEESE, QHK RANCH, ALL<br>WRAPPED IN A WHOLE<br>WHEAT TORTILLA.</p>

  <!-- Lunch / Dinner -->
  <section class="abs panel" style="left:575px;top:377px;width:371px;height:302px;"></section>
  <h2 class="abs panel-title" style="left:670px;top:366px;width:182px;font-size:18px;line-height:22px;">LUNCH/DINNER</h2>
  <div class="abs dish-thumb thumb-pasta" style="left:580px;top:384px;width:80px;height:80px;" role="img" aria-label="Plate of penne pasta with salad"></div>
  <div class="abs dish-thumb thumb-pasta" style="left:860px;top:384px;width:80px;height:80px;" role="img" aria-label="Plate of penne pasta with salad"></div>
  <div class="abs section-tag" style="left:662px;top:403px;width:192px;height:42px;line-height:38px;">MEAL PREP ITEMS</div>

  <div class="abs line-name" style="left:587px;top:499px;">BBQ GLAZED<br>SALMON</div>
  <div class="abs line-price" style="left:690px;top:502px;">$16.50</div>
  <div class="abs line-name" style="left:587px;top:541px;">CHEESEBURGER<br>BOWL</div>
  <div class="abs line-price" style="left:690px;top:544px;">$13.50</div>
  <div class="abs line-name" style="left:587px;top:582px;">CHICKEN ALFREDO</div>
  <div class="abs line-price" style="left:690px;top:580px;">$12.00</div>
  <div class="abs line-name" style="left:587px;top:610px;">PESTO CHICKEN<br>PASTA</div>
  <div class="abs line-price" style="left:690px;top:613px;">$12.00</div>

  <div class="abs col-rule" style="left:760px;top:496px;height:146px;"></div>

  <div class="abs line-name" style="left:772px;top:494px;">CHICKEN PARMESAN</div>
  <div class="abs line-price" style="left:871px;top:492px;">$13.00</div>
  <div class="abs line-name" style="left:772px;top:519px;">TACO BOWL</div>
  <div class="abs line-price" style="left:871px;top:517px;">$14.00</div>
  <div class="abs line-name" style="left:772px;top:544px;">STEAK BITE AND<br>GREEN STIR FRY</div>
  <div class="abs line-price" style="left:871px;top:548px;">$12.00</div>
  <div class="abs line-name" style="left:772px;top:585px;">ASIAN CHICKEN<br>TERIYAKI</div>
  <div class="abs line-price" style="left:871px;top:589px;">$12.00</div>
  <div class="abs line-name" style="left:772px;top:626px;">MARLOWE STIR FRY</div>
  <div class="abs line-price" style="left:871px;top:624px;">$15.95</div>
</main>
</body>
</html>
```